Kelvane Plumbing Business cards

Company is Kelvane Plumbing.
name Dashel Morrowby, I am a plumber, drainer, gasfitter and roofer
Mobile: 0431 906 154
Email address: info@kelvaneplumbing.example (check out my website for some ideas)
Website: www.kelvaneplumbing.example
ABN: 82 916 203 471
LIC: 604517K

I am reliable all round plumber. I am a 24 hour emergency service. Kelvane Plumbing is a professional plumbing service in the Illawarra, South Coast, Southern Sydney and Southern Highland regions of NSW. We offer a 24 hour emergency service for piece of mind to our customers. Call us now to see how we can help you. Kelvane Plumbing approaches every job with attention to detail and excellent customer service. With our superior workmanship you can be confident that the job will be done right the first time around. You can rest assured with results that are guaranteed to last.

Target Market(s)

the general public

Contact Information for Business Card

look up website for some ideas something with similar colours to logo and new modern and to catch the eye.

Colors
fdfdfd
ffffff
000000
7f7f7f
aaaaaa
33a6d7
0492cd

Requirements
Must have
• all contact details
• company- Kelvane Plumbing
• name- Dashel Morrowby
• number mobile- 0431 906 154
• Email address- info@kelvaneplumbing.example
• Website- www.kelvaneplumbing.example
• ABN- 82 916 203 471
• LIC- 604517K

```html
<!DOCTYPE html>
<html lang="en">
<head>
<meta charset="utf-8">
<title>Kelvane Plumbing Business Cards</title>
<link href="https://fonts.googleapis.com/css2?family=Montserrat:ital,wght@0,400;0,600;0,700;0,800;1,600&display=swap" rel="stylesheet">
<style>
  :root {
    --stage: #2b2b2b;
    --paper: #ffffff;
    --ink: #000000;
    --charcoal: #333333;
    --grey: #7f7f7f;
    --grey-light: #aaaaaa;
    --blue: #0492cd;
    --blue-soft: #33a6d7;
  }
  * { margin: 0; padding: 0; box-sizing: border-box; }
  html, body { width: 1200px; height: 1200px; overflow: hidden; }
  body {
    background: var(--stage);
    font-family: "Montserrat", Arial, sans-serif;
    display: flex;
    flex-direction: column;
    align-items: center;
    justify-content: center;
    gap: 36px;
  }
  .card {
    width: 900px;
    height: 514px;
    position: relative;
    overflow: hidden;
  }

  /* Front */
  .card-front {
    background: var(--paper);
    color: var(--ink);
    display: flex;
    flex-direction: column;
    align-items: center;
  }
  .front-mark {
    margin-top: 90px;
    display: flex;
    align-items: center;
    gap: 18px;
    color: var(--charcoal);
    font-weight: 700;
    font-size: 34px;
    letter-spacing: 0.04em;
    text-transform: uppercase;
  }
  .mark-dot {
    width: 30px;
    height: 30px;
    border-radius: 50%;
    background: var(--charcoal);
  }
  .front-title {
    margin-top: 110px;
    font-weight: 800;
    font-size: 68px;
    letter-spacing: 0.01em;
    text-transform: uppercase;
    white-space: nowrap;
  }
  .front-reg {
    margin-top: 8px;
    font-weight: 700;
    font-size: 27px;
    letter-spacing: 0.14em;
    white-space: nowrap;
  }
  .front-reg span + span { margin-left: 28px; }

  /* Back */
  .card-back {
    background: var(--ink);
    color: var(--paper);
  }
  .back-mark {
    position: absolute;
    left: 40px;
    top: 292px;
    width: 300px;
    text-align: center;
    color: var(--blue-soft);
    font-weight: 700;
    font-size: 26px;
    letter-spacing: 0.05em;
    text-transform: uppercase;
  }
  .back-mark .mark-dot {
    display: block;
    margin: 0 auto 16px;
    background: var(--blue-soft);
  }
  .holder {
    position: absolute;
    left: 420px;
    top: 64px;
    white-space: nowrap;
  }
  .holder-name {
    color: var(--blue);
    font-weight: 700;
    font-size: 34px;
    text-transform: uppercase;
    letter-spacing: 0.005em;
  }
  .holder-role {
    margin-top: 6px;
    color: var(--grey);
    font-weight: 400;
    font-size: 15px;
  }
  .contacts {
    position: absolute;
    left: 420px;
    top: 318px;
    list-style: none;
    white-space: nowrap;
  }
  .contacts li {
    display: flex;
    align-items: center;
    gap: 12px;
    height: 42px;
  }
  .contacts svg { width: 26px; height: 22px; flex: none; }
  .contact-phone { font-weight: 700; font-size: 24px; }
  .contact-link { font-weight: 600; font-style: italic; font-size: 22px; }
</style>
</head>
<body>

  <section class="card card-front">
    <div class="front-mark"><span class="mark-dot"></span>Kelvane Plumbing</div>
    <h1 class="front-title">Kelvane Plumbing</h1>
    <p class="front-reg"><span>ABN: 82 916 203 471</span><span>LIC: 604517K</span></p>
  </section>

  <section class="card card-back">
    <div class="back-mark"><span class="mark-dot"></span>Kelvane Plumbing</div>

    <div class="holder">
      <h2 class="holder-name">Dashel Morrowby</h2>
      <p class="holder-role">I am a plumber, drainer, gasfitter and roofer</p>
    </div>

    <ul class="contacts">
      <li>
        <svg viewBox="0 0 28 24" aria-hidden="true">
          <path d="M2 8c0-4 6-6 12-6s12 2 12 6v2h-7V7H9v3H2z" fill="#fff"/>
          <path d="M7 11h14l4 11H3z" fill="#fff"/>
          <circle cx="14" cy="16" r="3" fill="#000"/>
        </svg>
        <span class="contact-phone">0431 906 154</span>
      </li>
      <li>
        <svg viewBox="0 0 28 24" aria-hidden="true">
          <rect x="2" y="4" width="24" height="16" fill="none" stroke="#fff" stroke-width="1.6"/>
          <path d="M2 4l12 9 12-9M2 20l9-8M26 20l-9-8" fill="none" stroke="#fff" stroke-width="1.6"/>
        </svg>
        <span class="contact-link">info@kelvaneplumbing.example</span>
      </li>
      <li>
        <svg viewBox="0 0 28 24" aria-hidden="true">
          <g fill="none" stroke="#fff" stroke-width="1.4">
            <circle cx="14" cy="12" r="10"/>
            <ellipse cx="14" cy="12" rx="4.5" ry="10"/>
            <path d="M4 12h20M6 7h16M6 17h16"/>
          </g>
        </svg>
        <span class="contact-link">www.kelvaneplumbing.example</span>
      </li>
    </ul>
  </section>

</body>
</html>
```